Business Card for Freelance Copywriting & Web Design Business

Hi! I have a logo but want a new business card. Here's a better idea of what I'm thinking:
-Brand new double-sided business card, rounded cards, embossed logo, nice quality paper
-Include phone (604-382-9145), email (hello@linnearowatt.org), and website (www.linnearowatt.org). No address, please, since I service clients worldwide.
-I'd like the fonts to match those on my website (www.linnearowatt.org). I had to purchase the one font (Born Ready), attached. I'm not sure which version was used on my site so I included all that I purchased. The secondary font is Helvetica
-I'd also like the tagline "Powerful Words. Impressive Results." included.
-My primary brand colour is the teal, colour #19ADC3
Linnea Rowatt | Linnea Rowatt Copywriting & Web Design <hello@linnearowatt.org>
-I'd also like the following services listed on the new cards:
SEO Website Content
SEO Blog Content
SEO Website Design
Contact Information for Business Card
as stated in brief
Font styles to use
Other font styles liked:
- See brief
Look and feel
Each slider illustrates characteristics of the customer's brand and the style your logo design should communicate.

```html
<!DOCTYPE html>
<html lang="en">
<head>
<meta charset="utf-8">
<title>Linnea Rowatt — Business Card</title>
<link rel="stylesheet" href="https://fonts.googleapis.com/css2?family=Arimo:wght@400;700&display=swap">
<style>
  :root {
    --page: #e9eaeb;
    --card-white: #ffffff;
    --card-teal: #27666d;
    --ink: #1c1c1c;
    --brand: #2a6a73;
    --rule: #3a3a3a;
    --on-teal: #ffffff;
    --wordmark: #2f3d40;
  }
  * { box-sizing: border-box; margin: 0; padding: 0; }
  html, body { width: 1200px; height: 1000px; overflow: hidden; }
  body {
    background: var(--page);
    font-family: "Arimo", Helvetica, Arial, sans-serif;
    color: var(--ink);
    position: relative;
  }
  .card {
    position: absolute;
    top: 250px;
    width: 520px;
    height: 297px;
    border-radius: 14px;
    box-shadow: 0 6px 18px rgba(0,0,0,.18);
    overflow: hidden;
  }
  .card--front { left: 60px; background: var(--card-white); }
  .card--back  { left: 620px; background: var(--card-teal); color: var(--on-teal); }

  .front__name {
    position: absolute; left: 50px; top: 58px;
    font-size: 25px; color: var(--brand); font-weight: 400;
  }
  .front__role {
    position: absolute; left: 52px; top: 92px;
    font-size: 13px; color: var(--ink);
  }
  .front__rule {
    position: absolute; left: 60px; top: 142px;
    width: 62px; height: 1.5px; background: var(--rule);
  }
  .front__contacts {
    position: absolute; left: 66px; top: 172px;
    list-style: none; font-size: 17px; line-height: 25px;
  }
  .front__label { display: inline-block; width: 40px; }
  .front__web {
    position: absolute; left: 78px; top: 238px;
    font-size: 18px; color: var(--brand);
  }

  .back__lockup {
    position: absolute; left: 0; right: 0; top: 104px;
    text-align: center;
  }
  .back__mark {
    display: inline-flex; align-items: center; gap: 10px;
    font-size: 30px; font-weight: 400;
  }
  .back__dot {
    width: 12px; height: 12px; border-radius: 50%; background: var(--on-teal);
  }
  .back__tagline {
    margin-top: 8px; font-size: 11px; letter-spacing: 2px; font-weight: 700;
  }
  .back__services {
    position: absolute; left: 0; right: 0; bottom: 40px;
    text-align: center; font-size: 11px;
  }
  .back__services span + span::before { content: " | "; padding: 0 4px; }

  .wordmark {
    position: absolute; left: 0; right: 0; top: 690px;
    text-align: center; color: var(--wordmark);
  }
  .wordmark__name {
    display: inline-flex; align-items: center; gap: 14px;
    font-size: 56px; font-weight: 400;
  }
  .wordmark__dot {
    width: 20px; height: 20px; border-radius: 50%; background: var(--brand);
  }
  .wordmark__tagline {
    margin-top: 12px; font-size: 15px; letter-spacing: 3px; font-weight: 700;
  }
</style>
</head>
<body>
  <section class="card card--front" aria-label="Card front">
    <h1 class="front__name">Linnea Rowatt</h1>
    <p class="front__role">Copywriting &amp; Web Design</p>
    <div class="front__rule"></div>
    <ul class="front__contacts">
      <li><span class="front__label">P :</span>604-382-9145</li>
      <li><span class="front__label">E :</span>hello@linnearowatt.org</li>
    </ul>
    <p class="front__web">www.linnearowatt.org</p>
  </section>

  <section class="card card--back" aria-label="Card back">
    <div class="back__lockup">
      <div class="back__mark"><span class="back__dot"></span>Linnea Rowatt</div>
      <p class="back__tagline">COPYWRITING &amp; WEB DESIGN</p>
    </div>
    <p class="back__services">
      <span>SEO Website Content</span><span>SEO Blog Content</span><span>SEO Website Design</span>
    </p>
  </section>

  <div class="wordmark">
    <div class="wordmark__name"><span class="wordmark__dot"></span>Linnea Rowatt</div>
    <p class="wordmark__tagline">COPYWRITING &amp; WEB DESIGN</p>
  </div>
</body>
</html>
```